Awesome Business Card Design needed!

Hey there.
I'm looking for a simple but awesome business card design.
Type of company: Online advertisement agency
(please don't use the typical business people or statistics images on the card)
The front has to display the business name
and possibly some sort of logo ( perhaps something with the two M's of the biz name )
And the back of the card should say:
Name
Phone
Email
Let your imagination flow.
here are some designs that I like and that you can use as inspiration.
Simple but Awesome
http://images.pixelvantor.net/designs/55128_877673_43091_thumbnail.jpg
http://images.pixelvantor.net/designs/37714_747642_40106_image.jpg
http://images.pixelvantor.net/designs/55128_877673_43091_image.jpg
http://images.pixelvantor.net/designs/51321_781878_43091_image.jpg
http://images.pixelvantor.net/designs/33378_399063_15912_image.jpg
http://images.pixelvantor.net/designs/2337_271604_9495_image.jpg
good luck

```html
<!DOCTYPE html>
<html lang="en">
<head>
<meta charset="utf-8">
<title>Velora Media – Business Cards</title>
<link rel="stylesheet" href="https://fonts.googleapis.com/css2?family=Michroma&display=swap">
<style>
  :root {
    --page-bg: #3a3b3d;
    --card-black: #0d0e10;
    --card-tile: #17191c;
    --brand-blue: #4a9be0;
    --text-silver: #d9dbde;
    --rule-silver: #8d9095;
  }
  * { margin: 0; padding: 0; box-sizing: border-box; }
  html, body {
    width: 1200px;
    height: 880px;
    overflow: hidden;
    background: var(--page-bg);
  }
  .sheet {
    width: 1200px;
    height: 880px;
    display: flex;
    flex-direction: column;
    align-items: center;
    justify-content: center;
    gap: 32px;
    font-family: "Michroma", sans-serif;
  }
  .card {
    position: relative;
    width: 640px;
    height: 366px;
    border-radius: 4px;
    overflow: hidden;
    background: var(--card-black);
    box-shadow: 0 14px 30px rgba(0, 0, 0, 0.45);
  }
  .card-texture {
    position: absolute;
    inset: 0;
    background: radial-gradient(ellipse at 40% 30%, var(--card-tile) 0%, var(--card-black) 75%);
  }
  .card-content {
    position: relative;
    height: 100%;
    display: flex;
    flex-direction: column;
    align-items: center;
    justify-content: center;
  }
  .brand {
    display: flex;
    align-items: center;
    gap: 16px;
    color: var(--brand-blue);
    font-weight: 400;
    letter-spacing: 0.04em;
    text-transform: uppercase;
  }
  .brand-square {
    background: var(--brand-blue);
    flex: none;
  }
  .card-front .brand { font-size: 34px; }
  .card-front .brand-square { width: 34px; height: 34px; }
  .card-back .brand { font-size: 20px; gap: 10px; margin-bottom: 34px; }
  .card-back .brand-square { width: 20px; height: 20px; }
  .contact {
    display: flex;
    flex-direction: column;
    align-items: flex-start;
    color: var(--text-silver);
    text-transform: uppercase;
  }
  .contact-name {
    font-size: 19px;
    letter-spacing: 0.03em;
    padding: 0 4px 6px;
    margin-bottom: 12px;
    border-bottom: 1px solid var(--rule-silver);
    align-self: center;
  }
  .contact-line {
    font-size: 13px;
    letter-spacing: 0.04em;
    line-height: 1.9;
  }
</style>
</head>
<body>
  <main class="sheet">
    <section class="card card-back">
      <div class="card-texture" role="img" aria-label="Dark tiled square pattern covering the card"></div>
      <div class="card-content">
        <div class="brand"><span class="brand-square"></span><span>Velora Media</span></div>
        <div class="contact">
          <p class="contact-name">Daniel Brooks</p>
          <p class="contact-line">P: 1221 480 7719</p>
          <p class="contact-line">E: info@veloramedia.com</p>
        </div>
      </div>
    </section>
    <section class="card card-front">
      <div class="card-texture" role="img" aria-label="Dark tiled square pattern covering the card"></div>
      <div class="card-content">
        <div class="brand"><span class="brand-square"></span><span>Velora Media</span></div>
      </div>
    </section>
  </main>
</body>
</html>
```